Morning Harvest Psalm Journal for the Weary Traveler on the Narrow Road

This is not an Eastern meditation method. No images or themes from guru style or Eastern meditations from Hinduism or Buddhism will work. This is a Biblical Christian-based method. Some sort of Divine Light from Heaven may be the look. Some "ancient scroll" for the title to be written in may work.

```html
<!DOCTYPE html>
<html lang="en">
<head>
<meta charset="utf-8">
<title>Morning Harvest Psalm Journal — Book Cover</title>
<link href="https://fonts.googleapis.com/css2?family=UnifrakturMaguntia&family=Cinzel:wght@400;500&family=Cormorant+SC:wght@500&display=swap" rel="stylesheet">
<style>
  :root {
    --sky-deep: #6b4415;
    --sky-mid: #b9822e;
    --sky-gold: #e7b85a;
    --sky-glow: #fff6dc;
    --parchment-light: #fffdf4;
    --parchment-mid: #f6e6bd;
    --parchment-edge: #d9b873;
    --ink: #4a2a10;
    --rule: #7a5326;
    --author: #fbeac2;
  }
  * { margin: 0; padding: 0; box-sizing: border-box; }
  html, body {
    width: 800px;
    height: 1200px;
    overflow: hidden;
    background: var(--sky-deep);
  }
  .cover {
    position: relative;
    width: 800px;
    height: 1200px;
    overflow: hidden;
  }
  .cover__sky {
    position: absolute;
    inset: 0;
    background:
      radial-gradient(ellipse 55% 40% at 50% 42%, var(--sky-glow) 0%, rgba(255,240,200,0.6) 35%, rgba(231,184,90,0) 70%),
      radial-gradient(ellipse 70% 30% at 50% 95%, var(--sky-gold) 0%, rgba(185,130,46,0) 80%),
      linear-gradient(180deg, var(--sky-mid) 0%, var(--sky-gold) 35%, var(--sky-gold) 60%, var(--sky-mid) 85%, var(--sky-deep) 100%);
  }
  .cover__scroll {
    position: absolute;
    left: 133px;
    top: 133px;
    width: 547px;
    height: 787px;
    border-radius: 14px;
    background:
      radial-gradient(ellipse 70% 60% at 50% 45%, var(--parchment-light) 0%, var(--parchment-mid) 70%, var(--parchment-edge) 100%);
    box-shadow: 0 0 60px rgba(255,250,230,0.8);
  }
  .title {
    position: absolute;
    left: 133px;
    top: 133px;
    width: 547px;
    height: 787px;
    text-align: center;
    color: var(--ink);
  }
  .title__rule {
    position: absolute;
    left: 140px;
    width: 267px;
    height: 2px;
    background: var(--rule);
  }
  .title__rule--top { top: 70px; }
  .title__rule--bottom { top: 640px; }
  .title__line {
    position: absolute;
    left: 0;
    width: 100%;
    font-family: "UnifrakturMaguntia", serif;
    font-weight: 400;
    line-height: 1;
    text-shadow: 0 0 6px rgba(255,255,255,0.9);
  }
  .title__line--1 { top: 95px; font-size: 82px; }
  .title__line--2 { top: 195px; font-size: 82px; }
  .title__line--hero { top: 285px; font-size: 150px; }
  .title__line--4 { top: 455px; font-size: 92px; }
  .title__subtitle {
    position: absolute;
    left: 0;
    top: 575px;
    width: 100%;
    font-family: "Cormorant SC", serif;
    font-weight: 500;
    font-size: 24px;
    letter-spacing: 0.5px;
  }
  .author {
    position: absolute;
    left: 0;
    top: 1048px;
    width: 100%;
    text-align: center;
    font-family: "Cinzel", serif;
    font-weight: 400;
    font-size: 56px;
    letter-spacing: 3px;
    color: var(--author);
    text-shadow: 0 2px 8px rgba(70,40,10,0.6);
  }
</style>
</head>
<body>
  <main class="cover">
    <div class="cover__sky" role="img" aria-label="Golden clouds parting around a burst of heavenly light"></div>
    <div class="cover__scroll" role="img" aria-label="Glowing unrolled ancient parchment scroll with curled ends and corner flourishes"></div>
    <h1 class="title">
      <span class="title__rule title__rule--top"></span>
      <span class="title__line title__line--1">Morning</span>
      <span class="title__line title__line--2">Harvest</span>
      <span class="title__line title__line--hero">Psalm</span>
      <span class="title__line title__line--4">Journal</span>
      <span class="title__subtitle">FOR THE WEARY TRAVELER ON THE NARROW ROAD</span>
      <span class="title__rule title__rule--bottom"></span>
    </h1>
    <p class="author">SAMUEL WHITMORE</p>
  </main>
</body>
</html>
```